Korvel Reefworks business card

We sell live saltwater fish and live corals
Korvel Reefworks
7 Halden Ct
Dunmore, NJ. 08417
(856) 319-7264
Contact Information for Business Card
Korvel Reefworks
7 Halden Ct
Dunmore, NJ. 08417
(856) 319-7264
Colors
Designer to choose colors to be used in the design.

```html
<!DOCTYPE html>
<html lang="en">
<head>
<meta charset="UTF-8">
<title>Korvel Reefworks Business Card</title>
<link href="https://fonts.googleapis.com/css2?family=Montserrat:wght@300;800&display=swap" rel="stylesheet">
<style>
  :root {
    --page: #ffffff;
    --sky-top: #0dbfc1;
    --sky-mid: #8fe0df;
    --sky-bottom: #ffffff;
    --sea-top: #04abbd;
    --sea-bottom: #07bec1;
    --sand: #d9a96d;
    --ink: #000000;
    --icon-line: #07b8c0;
  }
  html, body {
    margin: 0;
    padding: 0;
    width: 1200px;
    height: 1200px;
    overflow: hidden;
    background: var(--page);
  }
  .canvas {
    position: relative;
    width: 1200px;
    height: 1200px;
  }
  .card {
    position: absolute;
    left: 100px;
    top: 300px;
    width: 1000px;
    height: 600px;
    overflow: hidden;
    font-family: "Montserrat", sans-serif;
    color: var(--ink);
  }
  .card__sky {
    position: absolute;
    left: 0; top: 0;
    width: 100%;
    height: 248px;
    background: linear-gradient(to bottom, var(--sky-top) 0%, var(--sky-mid) 45%, var(--sky-bottom) 92%);
  }
  .card__sea {
    position: absolute;
    left: 0; top: 248px;
    width: 100%;
    height: 278px;
    background: linear-gradient(to bottom, var(--sea-top), var(--sea-bottom));
  }
  .card__sand {
    position: absolute;
    left: 0; top: 526px;
    width: 100%;
    height: 74px;
    background: var(--sand);
  }
  .card__boat {
    position: absolute;
    left: 814px;
    top: 207px;
    width: 46px;
    height: 41px;
    background: var(--ink);
    border-radius: 50% 50% 4px 4px;
  }
  .card__name {
    position: absolute;
    left: 0; top: 189px;
    width: 100%;
    text-align: center;
    font-weight: 800;
    font-size: 38px;
    line-height: 48px;
    margin: 0;
  }
  .card__address {
    position: absolute;
    left: 0; top: 259px;
    width: 100%;
    text-align: center;
    font-weight: 300;
    font-size: 30px;
    line-height: 36px;
    margin: 0;
    font-style: normal;
  }
  .card__phone-icon {
    position: absolute;
    left: 472px;
    top: 357px;
    width: 56px;
    height: 56px;
  }
  .card__phone {
    position: absolute;
    left: 0; top: 419px;
    width: 100%;
    text-align: center;
    font-weight: 300;
    font-size: 30px;
    line-height: 36px;
    margin: 0;
  }
</style>
</head>
<body>
<div class="canvas">
  <section class="card" aria-label="Korvel Reefworks business card">
    <div class="card__sky"></div>
    <div class="card__sea"></div>
    <div class="card__sand"></div>
    <div class="card__boat" role="img" aria-label="Small sailboat silhouette on the horizon"></div>

    <h1 class="card__name">Korvel Reefworks</h1>
    <address class="card__address">7 Halden Ct<br>Dunmore, NJ. 08417</address>

    <svg class="card__phone-icon" viewBox="0 0 54 54" aria-hidden="true">
      <circle cx="27" cy="27" r="27" fill="var(--ink)"/>
      <rect x="18" y="11" width="18" height="32" rx="3" fill="var(--icon-line)"/>
      <rect x="20" y="15" width="14" height="22" fill="var(--ink)"/>
      <rect x="24" y="12.5" width="6" height="1.2" rx="0.6" fill="var(--ink)"/>
      <circle cx="27" cy="40" r="1.6" fill="var(--ink)"/>
    </svg>

    <p class="card__phone">(856) 319-7264</p>
  </section>
</div>
</body>
</html>
```